Fernvale Craft Works business card design- Fine Art sculpture business (Contract guaranteed)

This business card is for a fine art business. Though we don't have a website up and running yet it should be up soon. I would like the business card to be elegant and fairly simple with a picture of one of my sculptures on the front (you might need to photoshop out the background) as well as my basic contact info (my name,phone # and e-mail). On the back I'd like it to be pretty simple with just "Notes" and some blank lines for writing in info.

Target Market(s)

High end artwork buyers

Industry/Entity Type

Art Gallery

Contact Information for Business Card

Marlo Prewitt Phone: (555) 213-4098 E-mail: marlo@quillbrookmail.com Facebook: @fernvalecraftworks Instagram: fernvalecraftworks

Colors

Designer to choose colors to be used in the design.

Requirements
Must have
• *A picture of one of my sculptures*, my name, business name (Fernvale Craft Works), e-mail, phone #, and a notes section on the back.
• Fernvale Craft Works
• Marlo Prewitt
• (555)213-4098
• marlo@quillbrookmail.com
• Facebook: @fernvalecraftworks
• Instagram: fernvalecraftworks
Nice to have
• It'd be nice if you can crop out the background in the sculpture pictures, which ever one you end up using.

```html
<!DOCTYPE html>
<html lang="en">
<head>
<meta charset="utf-8">
<title>Fernvale Craft Works – Business Card</title>
<link rel="stylesheet" href="https://fonts.googleapis.com/css2?family=Roboto:wght@300;400;500&display=swap">
<style>
  :root {
    --stage: #2b2b2d;
    --paper: #ffffff;
    --ink: #1c1c1c;
    --rule: #3a3a3a;
    --accent: #6a48a8;
    --photo-dark: #17181c;
    --photo-mid: #3c3a4a;
    --photo-light: #6f6a7e;
    --on-photo: #f2f2f2;
  }
  * { box-sizing: border-box; margin: 0; padding: 0; }
  html, body { width: 1200px; height: 896px; overflow: hidden; }
  body {
    background: var(--stage);
    font-family: 'Roboto', Arial, sans-serif;
    display: flex; align-items: center; justify-content: center; gap: 48px;
  }
  .card {
    position: relative; width: 540px; height: 309px;
    border-radius: 20px; overflow: hidden; background: var(--paper);
    box-shadow: 0 10px 30px rgba(0,0,0,.45);
  }
  .wordmark { display: flex; align-items: center; gap: 10px; }
  .wordmark__dot { width: 22px; height: 22px; border-radius: 50%; background: var(--accent); flex: none; }
  .wordmark__name { font-weight: 500; color: var(--ink); white-space: nowrap; }
  .tagline {
    display: flex; align-items: center; gap: 8px;
    font-size: 6.5px; letter-spacing: .12em; text-transform: uppercase; color: var(--ink);
  }
  .tagline::before { content: ""; width: 40px; height: 1px; background: var(--rule); }

  /* back */
  .card--back .brand { position: absolute; left: 36px; top: 32px; }
  .card--back .wordmark__name { font-size: 17px; }
  .card--back .tagline { margin-top: 8px; font-size: 6.5px; }
  .notes { position: absolute; left: 36px; right: 36px; top: 92px; }
  .notes__row { display: flex; align-items: flex-end; height: 40px; }
  .notes__label { font-size: 12px; font-weight: 500; letter-spacing: .06em; margin-right: 6px; }
  .notes__line { flex: 1; border-bottom: 1.5px solid var(--rule); }
  .notes__row--indent { padding-left: 64px; }
  .check-out {
    position: absolute; right: 36px; bottom: 22px; text-align: right; color: var(--ink);
  }
  .check-out__title { font-size: 12px; font-weight: 500; letter-spacing: .06em; margin-bottom: 4px; }
  .check-out__item { font-size: 11px; font-weight: 400; line-height: 1.4; }

  /* front */
  .card--front .photo { position: absolute; inset: 0; }
  .card--front .brand { position: absolute; right: 30px; top: 58px; text-align: right; }
  .card--front .wordmark__name { font-size: 26px; }
  .card--front .tagline { margin-top: 10px; justify-content: flex-end; }
  .contact { position: absolute; left: 30px; bottom: 20px; color: var(--on-photo); }
  .contact__name { font-size: 17px; font-weight: 500; letter-spacing: .04em; text-transform: uppercase; }
  .contact__role { font-size: 11px; font-weight: 300; margin-bottom: 8px; }
  .contact__address { font-size: 11px; font-weight: 300; line-height: 1.35; margin-bottom: 6px; }
  .contact__list { list-style: none; font-size: 11px; font-weight: 300; line-height: 1.45; }
  .contact__list li { display: flex; align-items: center; gap: 6px; white-space: nowrap; }
  .contact__list svg { width: 9px; height: 9px; fill: var(--on-photo); flex: none; }
  .contact__bullet { width: 9px; display: flex; justify-content: center; flex: none; }
  .contact__bullet::before { content: ""; width: 5px; height: 5px; border-radius: 50%; background: var(--on-photo); }
</style>
</head>
<body>

<section class="card card--back" aria-label="Card back">
  <div class="brand">
    <div class="wordmark"><span class="wordmark__dot"></span><span class="wordmark__name">Fernvale Craft Works</span></div>
    <p class="tagline">Not just stone, it is craft</p>
  </div>
  <div class="notes">
    <div class="notes__row"><span class="notes__label">NOTES</span><span class="notes__line"></span></div>
    <div class="notes__row notes__row--indent"><span class="notes__line"></span></div>
    <div class="notes__row notes__row--indent"><span class="notes__line"></span></div>
  </div>
  <div class="check-out">
    <p class="check-out__title">YOU CAN CHECK OUT</p>
    <p class="check-out__item">Facebook: @fernvalecraftworks</p>
    <p class="check-out__item">Instagram: fernvalecraftworks</p>
  </div>
</section>

<section class="card card--front" aria-label="Card front">
  <svg class="photo" viewBox="0 0 540 309" preserveAspectRatio="none">
    <defs>
      <linearGradient id="photoTone" x1="0" y1="1" x2="1" y2="0">
        <stop offset="0" stop-color="var(--photo-dark)"/>
        <stop offset=".55" stop-color="var(--photo-mid)"/>
        <stop offset="1" stop-color="var(--photo-light)"/>
      </linearGradient>
    </defs>
    <path role="img" aria-label="Photo of a stone sculpture"
          d="M0 0 H150 C230 60 230 200 330 240 C380 262 430 280 440 309 H0 Z" fill="url(#photoTone)"/>
    <path d="M150 0 C230 60 230 200 330 240 C380 262 430 280 440 309" fill="none" stroke="var(--accent)" stroke-width="4"/>
  </svg>

  <div class="brand">
    <div class="wordmark"><span class="wordmark__dot"></span><span class="wordmark__name">Fernvale Craft Works</span></div>
    <p class="tagline">Not just stone, it is craft</p>
  </div>

  <div class="contact">
    <p class="contact__name">Marlo Prewitt</p>
    <p class="contact__role">Director</p>
    <p class="contact__address">PO box 440918<br>Alder Falls CO 80999</p>
    <ul class="contact__list">
      <li><svg viewBox="0 0 10 10"><path d="M2 0.5 L3.6 2.6 L2.7 3.8 C3.4 5.2 4.8 6.6 6.2 7.3 L7.4 6.4 L9.5 8 L8.4 9.5 C4.5 9.2 0.8 5.5 0.5 1.6 Z"/></svg>(555) 213-4098</li>
      <li><svg viewBox="0 0 10 10"><path d="M0.5 2 H9.5 V8 H0.5 Z M1.2 2.6 L5 5.4 L8.8 2.6" fill="none" stroke="#f2f2f2" stroke-width="1"/></svg>marlo@quillbrookmail.com</li>
      <li><span class="contact__bullet"></span>Facebook: @fernvalecraftworks</li>
      <li><span class="contact__bullet"></span>Instagram: fernvalecraftworks</li>
    </ul>
  </div>
</section>

</body>
</html>
```